Dr Selwyn aesthetics - Radiance Refined

I need a logo design for a new aesthetics business in London. I am specialised in Botox, Dermal Fillers & Skin Pigmentation treatment. The slogan is Radiance Refined. I would like some of the writing on the card to be embossed. I would like a very elegant design with the following detail:

1. White and gray scale background. For the font colour try gold OR silver shades.
2. The business involves working on the face mostly. Anything that can be done with letter 'M'? Or any other logo?
3. The front of the card should have Dr Selwyn Aesthetics and the slogan 'Radiance Refined'. The back should have my full name (Dr Selwyn Tarkett), qualifications (MBBS MSC BSC), my website (www.thebrindlecliniccollective.example), telephone number & email.
4. The back should also say treatments offered: ANTI-WRINKLE INJECTIONS. DERMAL FILLERS, LIP ENHANCEMENT, HYPERHYDROSIS. SKIN PIGMENTATION

Thank you very much
Updates

Project Deadline Extended
Reason: Delays in market research response. I would be grateful for an extension please. Many thanks

Target Market(s)

Female and male aged 18 and above

Industry/Entity Type

Business

Contact Information for Business Card

Elegant design. Square corners. British standard size. Horizontal design. Should contain the slogan, contact details.

Font styles to use
Script

Colors
c9c9c9
fbed22
ffffff
f5f5f5
000000

Requirements
Must have
• All that's mentioned above
Nice to have
• A logo with the outline of a female face. Or anything that can be done with the letter M of Selwyn.
Should not have
• No colours like green / purple / orange

```html
<!DOCTYPE html>
<html lang="en">
<head>
<meta charset="utf-8">
<title>Dr Selwyn Aesthetics – Business Card</title>
<link rel="stylesheet" href="https://fonts.googleapis.com/css2?family=Lobster&family=Roboto:ital,wght@0,300;0,400;0,500;1,300&display=swap">
<style>
  :root {
    --page: #ffffff;
    --silver-top: #a9a9a9;
    --silver-mid: #cfcfcf;
    --silver-light: #f5f5f5;
    --figure: #c9c9c9;
    --figure-glow: #e6e6e6;
    --ink: #3a3a3a;
    --ink-soft: #4a4a4a;
    --band-dark: #333333;
    --band-text: #ffffff;
    --sans: "Roboto", Arial, sans-serif;
    --script: "Lobster", cursive;
  }
  * { margin: 0; padding: 0; box-sizing: border-box; }
  html, body { width: 922px; height: 1200px; overflow: hidden; background: var(--page); }
  .canvas { position: relative; width: 922px; height: 1200px; background: var(--page); }

  .card { position: absolute; left: 79px; width: 775px; height: 496px; overflow: hidden; }

  /* Front */
  .card--front {
    top: 68px;
    background: linear-gradient(to bottom, var(--silver-top) 0%, var(--silver-mid) 45%, var(--page) 100%);
  }
  .front__figure {
    position: absolute; left: 120px; top: 0; width: 560px; height: 496px;
    background: radial-gradient(ellipse 48% 52% at 52% 45%, var(--figure) 0%, var(--figure) 62%, var(--figure-glow) 78%, rgba(230,230,230,0) 100%);
  }
  .front__brand {
    position: absolute; left: 0; right: 0; top: 183px; text-align: center;
  }
  .brand__name {
    font-family: var(--sans); font-weight: 400; font-size: 20px;
    letter-spacing: 0.24em; color: var(--ink);
  }
  .brand__slogan {
    font-family: var(--script); font-size: 48px; line-height: 1.1;
    color: var(--ink-soft); margin-top: 8px; margin-left: -40px;
  }

  /* Back */
  .card--back { top: 638px; background: var(--silver-light); }
  .back__header {
    position: absolute; left: 0; top: 0; width: 100%; height: 129px;
    background: linear-gradient(to bottom, #c4c4c4, #d8d8d8);
    text-align: center; padding-top: 24px;
  }
  .back__title {
    font-family: var(--sans); font-weight: 300; font-size: 31px;
    letter-spacing: 0.2em; color: var(--ink);
  }
  .back__slogan {
    font-family: var(--script); font-size: 34px; line-height: 1.1;
    color: var(--ink-soft); margin-top: 2px; margin-left: -30px;
  }
  .back__details {
    position: absolute; left: 0; top: 129px; width: 100%; height: 203px;
    background: linear-gradient(to bottom, #c2c2c2 0%, #e6e6e6 55%, #f7f7f7 100%);
    text-align: center; padding-top: 25px;
    font-family: var(--sans); color: var(--ink);
  }
  .details__person { font-size: 23px; letter-spacing: 0.14em; font-weight: 400; }
  .details__web { font-size: 21px; letter-spacing: 0.08em; font-style: italic; font-weight: 300; margin-top: 6px; }
  .details__contact { margin-top: 22px; font-size: 22px; letter-spacing: 0.12em; line-height: 1.35; font-weight: 300; }
  .details__label { font-weight: 500; }
  .back__treatments {
    position: absolute; left: 0; bottom: 0; width: 100%; height: 164px;
    background: var(--band-dark); color: var(--band-text);
    font-family: var(--sans); font-weight: 300; font-size: 21px;
    letter-spacing: 0.2em; text-align: center; padding-top: 28px; line-height: 1.6;
  }
  .treatment + .treatment { margin-left: 30px; }
</style>
</head>
<body>
<main class="canvas">
  <section class="card card--front" aria-label="Card front">
    <div class="front__figure" role="img" aria-label="Soft grey silhouette of a woman's head in profile with a ponytail"></div>
    <div class="front__brand">
      <p class="brand__name">DR SELWYN AESTHETICS</p>
      <p class="brand__slogan">Radiance Refined</p>
    </div>
  </section>

  <section class="card card--back" aria-label="Card back">
    <header class="back__header">
      <p class="back__title">DR SELWYN AESTHETICS</p>
      <p class="back__slogan">Radiance Refined</p>
    </header>
    <div class="back__details">
      <p class="details__person">Dr Selwyn Tarkett (MBBS MSC BSC)</p>
      <p class="details__web">www.thebrindlecliniccollective.example</p>
      <p class="details__contact">
        <span class="details__label">TEL:</span> 0400 987 654<br>
        <span class="details__label">EMAIL:</span> hello@selwynclinic.example
      </p>
    </div>
    <div class="back__treatments">
      <p><span class="treatment">ANTI-WRINKLE INJECTIONS</span></p>
      <p><span class="treatment">DERMAL FILLERS</span><span class="treatment">LIP ENHANCEMENT</span></p>
      <p><span class="treatment">HYPERHYDROSIS</span><span class="treatment">SKIN PIGMENTATION</span></p>
    </div>
  </section>
</main>
</body>
</html>
```